Design a poster for popular Wine Bar in Melbourne

PROJECT: A1 poster and A4

JOB DESCRIPTION; We are a popular Wine Bar in Melbourne, a classy establishment that is serving the most extensive wine selection in our region. Check out our site: www.ferrytidewell.com.au. We are looking for an "art nuevo" inspired poster, using bright block colours - please reference the example poster attached and this must as your inspiration and guide when designing the piece.

NAME OF EVENT: Cork Time Club

TAG LINE: “Choose more, try more, spend less and discover new wines"

WHATS GOING ON:
All our poured wines available by the half glass - 75ml
$5 cheese and charcuterie tasting plates.
$2 coffin Bay Oysters

WHEN:
Weekdays from 4pm -6pm
Saturdays from 2pm - 5pm

Look on the brighter side - your glass is half full.

VENUE INFORMATION:

Address; 42 Ridley Rd, Brookvale
Phone: 9027 4613
Email: info@ferrytidewell.com.au
www.ferrytidewell.com.au

Target Market(s)

25-50 lovers of fine wine and food

Industry/Entity Type

Event

Requirements
Must have
• The art nuevo styling much like the example poster we have attached. The company logo and all details of event must be represented. 2 block colours to be used and ensue the piece is high standard.

Images must be high resolution.

Poster must be completed in illustrator or photoshop

Ensure there is a 3mm internal and external bleed.
Should not have
• Images of people - we are wanting this to be a stylised piece using more abstract, artistic imagery in the styling referenced in the poster attached.

```html
<!DOCTYPE html>
<html lang="en">
<head>
<meta charset="utf-8">
<title>Cork Time Club – Ferrytide Well</title>
<link rel="stylesheet" href="https://fonts.googleapis.com/css2?family=Archivo+Black&family=Questrial&family=Arimo:wght@700&display=swap">
<style>
  :root {
    --wine-deep: #5e0c10;
    --wine: #8f1a1e;
    --wine-bright: #a6221f;
    --orange: #ff5a10;
    --orange-glow: #ff8a2a;
    --glass-dark: #2a1214;
    --glass-wine: #6a1c22;
    --ink: #141010;
    --white: #ffffff;
  }
  html, body {
    margin: 0;
    padding: 0;
    width: 900px;
    height: 1200px;
    overflow: hidden;
    background: var(--white);
  }
  .poster {
    position: relative;
    width: 900px;
    height: 1200px;
    overflow: hidden;
    background: var(--white);
    font-family: "Questrial", sans-serif;
    color: var(--ink);
  }
  .backdrop {
    position: absolute;
    left: 12px;
    top: 10px;
    width: 876px;
    height: 1178px;
  }
  .glass-art {
    position: absolute;
    left: 580px;
    top: 424px;
    width: 262px;
    height: 762px;
  }
  .brand {
    position: absolute;
    left: 104px;
    top: 118px;
    display: flex;
    align-items: center;
    gap: 12px;
    font-size: 44px;
    letter-spacing: 1px;
    color: var(--ink);
    line-height: 1;
  }
  .brand-mark {
    width: 18px;
    height: 18px;
    background: var(--ink);
  }
  .event-title {
    position: absolute;
    left: 0;
    width: 920px;
    top: 274px;
    margin: 0;
    text-align: center;
    font-family: "Archivo Black", sans-serif;
    font-weight: 400;
    font-size: 88px;
    letter-spacing: 1px;
    line-height: 1;
    color: var(--ink);
    text-shadow: -7px 8px 6px rgba(0,0,0,0.45);
  }
  .tagline {
    position: absolute;
    left: 0;
    width: 925px;
    top: 378px;
    margin: 0;
    text-align: center;
    font-family: "Arimo", sans-serif;
    font-weight: 700;
    font-size: 26px;
    color: var(--white);
    white-space: nowrap;
  }
  .section-label {
    position: absolute;
    left: 100px;
    margin: 0;
    font-size: 21px;
    font-weight: 400;
    text-transform: uppercase;
  }
  .copy {
    position: absolute;
    margin: 0;
    font-size: 22px;
    line-height: 1.2;
    white-space: nowrap;
  }
  .contact {
    position: absolute;
    left: 100px;
    top: 1046px;
    margin: 0;
    font-size: 21px;
    font-style: normal;
    line-height: 27px;
  }
</style>
</head>
<body>
<main class="poster">
  <svg class="backdrop" viewBox="0 0 876 1178" aria-hidden="true">
    <defs>
      <linearGradient id="wine-panel" x1="0" y1="0" x2="0.3" y2="1">
        <stop offset="0" stop-color="#9c1a20"/>
        <stop offset="0.55" stop-color="#86201c"/>
        <stop offset="1" stop-color="#6a1514"/>
      </linearGradient>
      <linearGradient id="wine-sweep" x1="0" y1="0" x2="1" y2="1">
        <stop offset="0" stop-color="#a8231f"/>
        <stop offset="0.5" stop-color="#9b3324"/>
        <stop offset="1" stop-color="#8a3a22"/>
      </linearGradient>
      <radialGradient id="orange-panel" cx="0.6" cy="0.6" r="0.8">
        <stop offset="0" stop-color="#ff8a2a"/>
        <stop offset="0.6" stop-color="#ff6414"/>
        <stop offset="1" stop-color="#ff5a10"/>
      </radialGradient>
    </defs>
    <rect class="panel-orange" x="568" y="0" width="308" height="1178" fill="url(#orange-panel)"/>
    <rect class="panel-wine" x="0" y="0" width="570" height="1178" fill="url(#wine-panel)"/>
    <path class="panel-sweep" d="M120 0 C40 160 0 380 40 600 C80 820 260 930 390 1000 C470 1045 500 1110 500 1178 L570 1178 L570 0 Z" fill="url(#wine-sweep)"/>
    <path class="panel-shade" d="M0 0 L120 0 C40 160 0 380 40 600 C60 700 50 720 0 730 Z" fill="#6e0d12" opacity="0.6"/>
    <path class="panel-corner" d="M0 960 C140 990 330 980 420 1040 C470 1075 490 1130 490 1178 L0 1178 Z" fill="var(--wine-deep)" opacity="0.85"/>
    <line x1="570" y1="0" x2="570" y2="1178" stroke="#5a0f10" stroke-width="2"/>
  </svg>

  <svg class="glass-art" viewBox="0 0 262 762" role="img" aria-label="Illustration area: stylised wine glass half filled with red wine, its tall bowl tapering into a thin stem and foot">
    <defs>
      <linearGradient id="glass-tone" x1="0" y1="0" x2="0" y2="1">
        <stop offset="0" stop-color="#3a1416"/>
        <stop offset="0.25" stop-color="#6a1c22"/>
        <stop offset="0.55" stop-color="#4a1a1c"/>
        <stop offset="1" stop-color="#1c1212"/>
      </linearGradient>
    </defs>
    <rect width="262" height="762" fill="url(#glass-tone)"/>
  </svg>

  <div class="brand">
    <span class="brand-mark"></span>
    <span class="brand-name">FERRYTIDE WELL</span>
  </div>

  <h1 class="event-title">Cork Time Club</h1>
  <p class="tagline">“Choose more, try more, spend less and discover new wines”</p>

  <h2 class="section-label" style="top:513px">Whats going on:</h2>
  <p class="copy" style="left:103px;top:555px">All our poured wines available by the half glass - 75ml</p>
  <p class="copy" style="left:134px;top:594px">$ 5 cheese and charcuterie tasting plates</p>
  <p class="copy" style="left:134px;top:633px">$ 2 Coffin Bay Oysters</p>

  <h2 class="section-label" style="top:784px">When:</h2>
  <p class="copy" style="left:100px;top:827px">Weekdays</p>
  <p class="copy" style="left:356px;top:827px">Saturdays</p>
  <p class="copy" style="left:101px;top:864px">from 4pm-6pm</p>
  <p class="copy" style="left:358px;top:866px">from 2pm-5pm</p>
  <p class="copy" style="left:100px;top:900px">Look on the brighter side - your glass is half full.</p>

  <h2 class="section-label" style="top:1015px">Venue information:</h2>
  <address class="contact">
    Address: 42 Ridley Rd, Brookvale<br>
    Phone: 9027 4613<br>
    Email: info@ferrytidewell.com.au<br>
    www.ferrytidewell.com.au
  </address>
</main>
</body>
</html>
```